Flyer for the Harvest Lantern Gathering 2018

Design a flyer for our annual conference with basic information about the conference: conference logo and year,

Location:
Dunmore Community Center (Downtown Portland)
482 Willowby Street, Portland, ME 04117,

Date:
August 24th, 25th and 26th, 2018
Start time 6:00PM

I would like the following three words added to the flyer. These words describe the vision of the conference:
Prophetic, Worship, Prayer

```html
<!DOCTYPE html>
<html lang="en">
<head>
<meta charset="utf-8">
<title>Harvest Lantern Gathering 2018 – Flyer</title>
<link rel="stylesheet" href="https://fonts.googleapis.com/css2?family=Forum&family=Arimo:wght@400&display=swap">
<style>
  :root {
    --page-bg: #f2f3f3;
    --paper: #ffffff;
    --ink: #2f3a3c;
    --gold: #e1ac22;
    --olive: #365a06;
    --photo-light: #e4e2df;
    --photo-mid: #a9a7a3;
    --photo-dark: #5f605e;
  }
  * { margin: 0; padding: 0; box-sizing: border-box; }
  html, body { width: 1200px; height: 1200px; overflow: hidden; background: var(--page-bg); }
  .flyer {
    position: absolute; left: 226px; top: 52px;
    width: 650px; height: 952px;
    transform: scale(1.152); transform-origin: top left;
    background: var(--paper); overflow: hidden;
  }
  .flyer__photo {
    position: absolute; left: 0; top: 0; width: 650px; height: 640px;
    background: linear-gradient(170deg, var(--photo-light) 0%, var(--photo-mid) 55%, var(--photo-dark) 100%);
  }
  .flyer__shapes { position: absolute; left: 0; top: 0; width: 650px; height: 952px; }
  .brand {
    position: absolute; left: 40px; top: 150px;
    font-family: "Forum", serif; font-size: 38px; letter-spacing: 1px;
    color: var(--ink); line-height: 1;
  }
  .vision {
    position: absolute; left: 246px; top: 573px; width: 260px;
    font-family: "Forum", serif; font-weight: 400; color: var(--ink);
    text-align: center; line-height: 1;
  }
  .vision__word { display: block; }
  .vision__word--prophetic { font-size: 40px; letter-spacing: 3px; }
  .vision__word--prayer { font-size: 64px; letter-spacing: 3px; margin-top: 0; }
  .vision__word--worship { font-size: 46px; letter-spacing: 3px; margin-top: -2px; }
  .details {
    position: absolute; left: 178px; top: 768px; width: 396px;
    font-family: "Arimo", sans-serif; color: var(--ink); text-align: center;
  }
  .details__date { font-size: 21px; }
  .details__time { font-size: 21px; margin-top: 14px; }
  .details__venue { font-size: 13.5px; line-height: 1.1; margin-top: 22px; }
</style>
</head>
<body>
  <main class="flyer">
    <div class="flyer__photo" role="img" aria-label="Muted photograph of an open Bible with a wooden rosary and cross on a weathered table"></div>

    <svg class="flyer__shapes" viewBox="0 0 650 952" aria-hidden="true">
      <polygon points="0,952 268,482 358,535 488,535 568,492 650,532 650,952" fill="var(--paper)"/>
      <polygon points="292,432 332,434 426,512 488,535 358,535 268,482" fill="var(--olive)"/>
      <polygon points="426,512 508,457 613,457 568,492 488,535" fill="var(--gold)"/>
      <polygon points="613,457 650,457 650,532 568,492" fill="var(--olive)"/>
      <polygon points="0,617 213,432 292,432 0,952" fill="var(--gold)"/>
    </svg>

    <p class="brand">Harvest Lantern</p>

    <h1 class="vision">
      <span class="vision__word vision__word--prophetic">PROPHETIC</span>
      <span class="vision__word vision__word--prayer">PRAYER</span>
      <span class="vision__word vision__word--worship">WORSHIP</span>
    </h1>

    <section class="details">
      <p class="details__date">August 24th, 25th and 26th, 2018</p>
      <p class="details__time">Start time 6:00PM</p>
      <p class="details__venue">Dunmore Community Center<br>(Downtown Portland)<br>482 Willowby Street, Portland,<br>ME 04117</p>
    </section>
  </main>
</body>
</html>
```